We need a business card design for a new company located in Brampton Ontario Canada. Our goal is to promote companies to use our service as an "External Program Management " firm taking their industrial product concepts " from prototype to production." We would like to use blue and yellow as our colors. Our skills include finding suppliers for prototype parts and developing them into supplying not only prototypes but the final production parts as well for our customer base.
Colin Treadway
Sales Manager
VORMEL Solutions Inc.
14 Hollowmere Lane
Brampton, Ontario L3P 8K2
Canada
Phone: 905-417-2956
Fax: 905-417-2956
website: www.vormelsolutions.example
Email: colin@vormelsolutions.example

```html
<!DOCTYPE html>
<html lang="en">
<head>
<meta charset="utf-8">
<title>VORMEL Solutions Inc. – Business Card</title>
<link rel="stylesheet" href="https://fonts.googleapis.com/css2?family=Tinos:wght@400;700&display=swap">
<style>
  :root {
    --backdrop: #e8e5e0;
    --card-white: #fbfbfb;
    --card-grey: #e6e6e6;
    --brand-blue: #3a3ab0;
    --band-blue-light: #4a4ac2;
    --band-blue-dark: #2a2a96;
    --rule-black: #1a1a1a;
    --text-grey: #3c3c3c;
    --text-white: #f4f4fb;
  }
  * { box-sizing: border-box; margin: 0; padding: 0; }
  html, body {
    width: 1200px; height: 1023px; overflow: hidden;
    background: var(--backdrop);
    font-family: "Tinos", "Times New Roman", serif;
  }
  .canvas { position: relative; width: 1200px; height: 1023px; }
  .card {
    position: absolute; left: 100px; top: 226px;
    width: 1000px; height: 571px;
    background: linear-gradient(180deg, var(--card-white), var(--card-grey));
    box-shadow: 0 18px 40px rgba(0,0,0,.25);
    overflow: hidden;
  }
  .logo {
    position: absolute; left: 64px; top: 64px;
    display: flex; align-items: flex-start; gap: 16px;
    width: 440px;
  }
  .logo-square { width: 30px; height: 30px; background: var(--brand-blue); flex: none; margin-top: 8px; }
  .logo-name {
    font-size: 44px; font-weight: 700; color: var(--brand-blue);
    letter-spacing: 1px; line-height: 1.1; max-width: 340px;
  }
  .website {
    position: absolute; left: 64px; top: 226px;
    font-size: 26px; color: #5a5aa8;
  }
  .person { position: absolute; left: 600px; top: 92px; }
  .person-name {
    font-size: 40px; font-weight: 700; color: var(--brand-blue);
    text-transform: uppercase; letter-spacing: 1px; white-space: nowrap;
  }
  .person-title { font-size: 28px; color: var(--text-grey); margin-top: 10px; }
  .rule-pair { position: absolute; left: 0; width: 100%; height: 14px; }
  .rule-pair::before, .rule-pair::after {
    content: ""; position: absolute; left: 0; width: 100%; background: var(--rule-black);
  }
  .rule-pair::before { top: 0; height: 4px; }
  .rule-pair::after { bottom: 0; height: 2px; }
  .rule-pair.top { top: 296px; }
  .rule-pair.bottom { top: 530px; }
  .band {
    position: absolute; left: 0; top: 310px; width: 100%; height: 220px;
    background: linear-gradient(115deg, var(--band-blue-light) 0%, var(--brand-blue) 45%, var(--band-blue-dark) 100%);
    color: var(--text-white);
  }
  .address { position: absolute; left: 64px; top: 50px; font-size: 24px; line-height: 1.35; }
  .address-label { font-weight: 700; }
  .contact-line { display: flex; align-items: center; gap: 10px; white-space: nowrap; }
  .indent { padding-left: 30px; }
  .contacts {
    position: absolute; left: 600px; top: 40px;
    font-size: 24px; line-height: 1.45;
  }
  .icon { width: 20px; height: 20px; flex: none; }
</style>
</head>
<body>
<div class="canvas">
  <div class="card">
    <div class="logo">
      <div class="logo-square"></div>
      <div class="logo-name">VORMEL Solutions Inc.</div>
    </div>
    <div class="website">www.vormelsolutions.example</div>

    <div class="person">
      <div class="person-name">Colin Treadway</div>
      <div class="person-title">Sales Manager</div>
    </div>

    <div class="rule-pair top"></div>

    <div class="band">
      <div class="address">
        <div class="address-label">Company Address:</div>
        <div class="contact-line">
          <svg class="icon" viewBox="0 0 20 20"><rect width="20" height="20" rx="3" fill="#fff"/><path d="M10 4a4 4 0 0 0-4 4c0 3 4 8 4 8s4-5 4-8a4 4 0 0 0-4-4zm0 5.5a1.5 1.5 0 1 1 0-3 1.5 1.5 0 0 1 0 3z" fill="#3a3ab0"/></svg>
          <span>14 Hollowmere Lane Brampton,</span>
        </div>
        <div class="indent">Ontario L3P 8K2 Canada</div>
      </div>

      <div class="contacts">
        <div class="contact-line">
          <svg class="icon" viewBox="0 0 20 20"><rect width="20" height="20" rx="3" fill="#fff"/><path d="M6 4h3l1 3-2 1c1 2 2 3 4 4l1-2 3 1v3c-6 1-11-4-10-10z" fill="#3a3ab0"/></svg>
          <span>905-417-2956</span>
        </div>
        <div class="contact-line">
          <svg class="icon" viewBox="0 0 20 20"><rect width="20" height="20" rx="3" fill="#fff"/><rect x="6" y="4" width="8" height="4" fill="#3a3ab0"/><rect x="4" y="8" width="12" height="6" rx="1" fill="#3a3ab0"/><rect x="6" y="12" width="8" height="4" fill="#fff" stroke="#3a3ab0"/></svg>
          <span>905-417-2956</span>
        </div>
        <div class="contact-line">
          <svg class="icon" viewBox="0 0 20 20"><rect width="20" height="20" rx="3" fill="#fff"/><rect x="4" y="6" width="12" height="8" fill="none" stroke="#3a3ab0" stroke-width="1.6"/><path d="M4 6l6 5 6-5" fill="none" stroke="#3a3ab0" stroke-width="1.6"/></svg>
          <span>colin@vormelsolutions.example</span>
        </div>
      </div>
    </div>

    <div class="rule-pair bottom"></div>
  </div>
</div>
</body>
</html>
```